TEQUILA LABEL DESIGN

We require a glass bottle label design for Tequila. The label will be a full wraparound on a round bottle. Size of labels should be 125 mm height, 250 mm height.

1) The name of the Tequila is CORVELDO, its a Spanish word in English means Fantasy.
2) The label has to be in Classic Retro Design
3) The Paper should be textured uncoated paper
4) Colors used should be Pantone Uncoated, there should spot laminations and Embossing at highlight points.
5) Please submit designs in different schemes like some with subtle blacks, browns, golds and other in vivid bright colors and golds / silvers.
6) There should be fantasy elements like mythological birds and animals, ornaments, statues, gods and others. There can be a combination of different fantasy elements or variations of a single element.
7) The labels will be a full wraparound on a round bottle (drawing and picture of bottle attached)
8) We have also attached some labels that we like, but you are free to use your own creativity.
Updates

The height of the label should be 120 mm and the width 250 mm. Leave 40 mm width in each side for legends, story, barcodes, maker name, etc.

Target Market(s)

Premium high end consumers age group 25-45

Industry/Entity Type

Alcobev

Font styles to use
Decorative
Script

Colors
FFC000
F8CF3A
FAE287
FDF2CF
FEFAEE

Requirements
Nice to have
• Fantasy Elements, mythological characters, owls, castles, witchcraft

```html
<!DOCTYPE html>
<html lang="en">
<head>
<meta charset="utf-8">
<title>Corveldo Tequila – Wraparound Label</title>
<link rel="stylesheet" href="https://fonts.googleapis.com/css2?family=Cinzel:wght@400;700;900&family=Kaushan+Script&family=Open+Sans+Condensed:wght@300&display=swap">
<style>
  :root{
    --bg-top:#f6f6f7;
    --bg-bottom:#a9abb0;
    --label-black:#060606;
    --panel-black:#0b0b0b;
    --panel-glow:#4a4a4a;
    --gold-deep:#9a6a12;
    --gold:#d29a2f;
    --gold-light:#f8cf3a;
    --gold-pale:#fae287;
    --cream:#fdf2cf;
    --ink:#0d0b08;
    --phoenix-hot:#f59a1c;
    --phoenix-deep:#b8470c;
    --legend-text:#c9c9c9;
    --white:#ffffff;
  }
  html,body{margin:0;padding:0;overflow:hidden;}
  body{
    width:1161px;height:1200px;
    background:linear-gradient(180deg,var(--bg-top),var(--bg-bottom));
  }
  .label-art{display:block;width:1161px;height:1200px;}
  .brand-name{
    font-family:"Kaushan Script",cursive;
    font-size:76px;
    fill:var(--gold-light);
  }
  .category{
    font-family:"Cinzel",serif;
    font-weight:900;
    font-size:46px;
    letter-spacing:20px;
    fill:var(--ink);
  }
  .volume-line{
    font-family:"Cinzel",serif;
    font-weight:700;
    font-size:20px;
    fill:var(--gold-pale);
  }
  .legend-text{
    font-family:"Open Sans Condensed","Arial Narrow",sans-serif;
    font-weight:300;
    font-size:12px;
    fill:var(--legend-text);
  }
</style>
</head>
<body>
<svg class="label-art" viewBox="0 0 1161 1200" xmlns="http://www.w3.org/2000/svg">
  <defs>
    <linearGradient id="goldFrame" x1="0" y1="0" x2="1" y2="0">
      <stop offset="0" stop-color="var(--gold-deep)"/>
      <stop offset="0.45" stop-color="var(--cream)"/>
      <stop offset="1" stop-color="var(--gold-deep)"/>
    </linearGradient>
    <linearGradient id="ribbonGold" x1="0" y1="0" x2="1" y2="0">
      <stop offset="0" stop-color="var(--gold-deep)"/>
      <stop offset="0.3" stop-color="var(--gold)"/>
      <stop offset="0.5" stop-color="var(--cream)"/>
      <stop offset="0.7" stop-color="var(--gold)"/>
      <stop offset="1" stop-color="var(--gold-deep)"/>
    </linearGradient>
    <radialGradient id="panelGlow" cx="0.5" cy="0.62" r="0.55">
      <stop offset="0" stop-color="var(--panel-glow)"/>
      <stop offset="1" stop-color="var(--panel-black)"/>
    </radialGradient>
    <linearGradient id="raysLeft" x1="1" y1="0" x2="0" y2="0">
      <stop offset="0" stop-color="#3a3a3a"/>
      <stop offset="1" stop-color="#101010"/>
    </linearGradient>
    <linearGradient id="raysRight" x1="0" y1="0" x2="1" y2="0">
      <stop offset="0" stop-color="#3a3a3a"/>
      <stop offset="1" stop-color="#101010"/>
    </linearGradient>
    <radialGradient id="phoenixFill" cx="0.5" cy="0.5" r="0.55">
      <stop offset="0" stop-color="var(--phoenix-hot)"/>
      <stop offset="1" stop-color="var(--phoenix-deep)" stop-opacity="0.85"/>
    </radialGradient>
    <filter id="labelShadow" x="-5%" y="-5%" width="115%" height="120%">
      <feDropShadow dx="6" dy="8" stdDeviation="6" flood-color="#000" flood-opacity="0.45"/>
    </filter>
    <path id="ribbonBaseline" d="M230,650 Q578,424 926,650"/>
  </defs>

  <!-- label body -->
  <g class="label" filter="url(#labelShadow)">
    <rect class="label-base" x="40" y="407" width="1080" height="520" fill="var(--label-black)"/>
    <path class="label-crown" d="M386,930 V330 Q386,270 446,270 H714 Q774,270 774,330 V930 Z" fill="var(--label-black)"/>
  </g>

  <!-- ray panels beside the crest -->
  <rect class="rays-left" x="300" y="650" width="86" height="190" fill="url(#raysLeft)"/>
  <rect class="rays-right" x="774" y="650" width="86" height="190" fill="url(#raysRight)"/>
  <line x1="300" y1="650" x2="300" y2="845" stroke="url(#goldFrame)" stroke-width="3"/>
  <line x1="860" y1="650" x2="860" y2="845" stroke="url(#goldFrame)" stroke-width="3"/>

  <!-- central crest panel -->
  <path class="crest-panel" d="M392,830 V340 Q392,282 450,282 H710 Q768,282 768,340 V830 Z"
        fill="url(#panelGlow)" stroke="url(#goldFrame)" stroke-width="6"/>

  <text class="brand-name" x="580" y="440" text-anchor="middle">Corveldo</text>

  <!-- phoenix crest illustration area -->
  <rect x="443" y="585" width="260" height="235" rx="20" fill="url(#phoenixFill)"
        role="img" aria-label="Illustration of a golden-orange phoenix with spread wings and flowing tail feathers"/>

  <!-- ribbon banner -->
  <path class="ribbon" d="M214,598 Q578,338 942,598 L942,690 Q578,434 214,690 Z" fill="url(#ribbonGold)"/>
  <path d="M214,598 L196,660 L214,690 Z" fill="var(--gold-deep)"/>
  <path d="M942,598 L960,660 L942,690 Z" fill="var(--gold-deep)"/>
  <text class="category"><textPath href="#ribbonBaseline" startOffset="50%" text-anchor="middle">TEQUILA</textPath></text>

  <!-- volume bar -->
  <rect class="volume-bar" x="300" y="851" width="563" height="72" fill="var(--label-black)" stroke="url(#goldFrame)" stroke-width="4"/>
  <text class="volume-line" x="330" y="896">ALC. 13.1% BY VOL.</text>
  <text class="volume-line" x="834" y="896" text-anchor="end">750ml</text>

  <!-- left legend panel -->
  <rect x="60" y="440" width="130" height="123" rx="14" fill="url(#phoenixFill)"
        role="img" aria-label="Small phoenix emblem illustration"/>
  <g class="legend-text">
    <text x="59" y="585">Text Example</text><text x="131" y="585">Text Example</text>
    <text x="59" y="605">Text Example</text><text x="131" y="605">Text Example</text>
    <text x="59" y="626">Text Example</text><text x="131" y="626">Text Example</text>
    <text x="59" y="646">Text Example</text><text x="131" y="646">Text Example</text>
    <text x="59" y="667">Text Example</text><text x="131" y="667">Text Example</text>
    <text x="59" y="687">Text Example</text><text x="131" y="687">Text Example</text>
    <text x="59" y="708">Text Example</text><text x="131" y="708">Text Example</text>
    <text x="59" y="728">Text Example</text><text x="131" y="728">Text Example</text>
    <text x="59" y="749">Text Example</text><text x="131" y="749">Text Example</text>
    <text x="59" y="769">Text Example</text><text x="131" y="769">Text Example</text>
    <text x="59" y="790">Text Example</text><text x="131" y="790">Text Example</text>
    <text x="59" y="810">Text Example</text><text x="131" y="810">Text Example</text>
    <text x="59" y="831">Text Example</text><text x="131" y="831">Text Example</text>
  </g>
  <rect class="legend-box" x="49" y="848" width="223" height="65" fill="var(--white)"/>

  <!-- right legend panel -->
  <rect x="966" y="440" width="130" height="123" rx="14" fill="url(#phoenixFill)"
        role="img" aria-label="Small phoenix emblem illustration"/>
  <g class="legend-text">
    <text x="966" y="585">Text Example</text><text x="1038" y="585">Text Example</text>
    <text x="966" y="605">Text Example</text><text x="1038" y="605">Text Example</text>
    <text x="966" y="626">Text Example</text><text x="1038" y="626">Text Example</text>
    <text x="966" y="646">Text Example</text><text x="1038" y="646">Text Example</text>
    <text x="966" y="667">Text Example</text><text x="1038" y="667">Text Example</text>
    <text x="966" y="687">Text Example</text><text x="1038" y="687">Text Example</text>
    <text x="966" y="708">Text Example</text><text x="1038" y="708">Text Example</text>
    <text x="966" y="728">Text Example</text><text x="1038" y="728">Text Example</text>
    <text x="966" y="749">Text Example</text><text x="1038" y="749">Text Example</text>
    <text x="966" y="769">Text Example</text><text x="1038" y="769">Text Example</text>
    <text x="966" y="790">Text Example</text><text x="1038" y="790">Text Example</text>
    <text x="966" y="810">Text Example</text><text x="1038" y="810">Text Example</text>
    <text x="966" y="831">Text Example</text><text x="1038" y="831">Text Example</text>
  </g>
  <rect class="legend-box" x="876" y="848" width="226" height="65" fill="var(--white)"/>
</svg>
</body>
</html>
```